IT services company needs a business card designed

-2 sided business card.-Front is going to be the logo raised (3D floating effect) on a black background. Make the logos spider web shiny silver and keep the spider the same design. -Back needs to have the following information:Darrel Sotho, Managing Partner, Cell: 738-402-1954, Website: Plankhorn.com, Email: Darrel@Plankhorn.com
Target Market(s)
IT Services
Industry/Entity Type
It Company
Contact Information for Business Card
-2 sided business card.
-Front is going to be the logo raised (3D floating effect) on a black background. Make the logos spider web shiny silver and keep the spider the same design.
-Back needs to have the following information:
Darrel Sotho, Managing Partner, Cell: 738-402-1954, Website: Plankhorn.com, Email: Darrel@Plankhorn.com

```html
<!DOCTYPE html>
<html lang="en">
<head>
<meta charset="utf-8">
<title>Plankhorn Business Card</title>
<link rel="stylesheet" href="https://fonts.googleapis.com/css2?family=Quicksand:wght@500;600&display=swap">
<style>
  :root {
    --backdrop: #d9dadc;
    --card: #121314;
    --card-edge: #1b1c1e;
    --silver: #c9cacc;
    --silver-dim: #8d8f93;
    --accent: #1fa3e0;
    --text-light: #e4e5e7;
  }
  * { margin: 0; padding: 0; box-sizing: border-box; }
  html, body {
    width: 1200px; height: 1189px; overflow: hidden;
    background: var(--backdrop);
    font-family: "Quicksand", sans-serif;
  }
  .sheet { position: relative; width: 1200px; height: 1189px; }
  .card {
    position: absolute; left: 120px; width: 960px; height: 549px;
    background: radial-gradient(ellipse at 60% 40%, var(--card-edge), var(--card) 70%);
    border-radius: 34px;
    overflow: hidden;
  }
  .card--front { top: 35px; }
  .card--back { top: 605px; }

  /* Front */
  .front-emblem {
    position: absolute; left: 380px; top: 70px; width: 200px; height: 200px;
    border-radius: 50%;
    background: radial-gradient(circle at 45% 40%, #dfe1e4, var(--silver-dim) 75%);
  }
  .front-wordmark {
    position: absolute; left: 0; right: 0; top: 310px; text-align: center;
    font-size: 78px; font-weight: 500; letter-spacing: 6px; color: var(--silver);
  }

  /* Back */
  .back-wordmark {
    position: absolute; left: 70px; top: 70px;
    font-size: 70px; font-weight: 500; letter-spacing: 5px; color: var(--silver);
  }
  .person { position: absolute; left: 78px; top: 200px; }
  .person-name {
    font-size: 34px; font-weight: 600; letter-spacing: 2px; color: var(--text-light);
    text-transform: uppercase; line-height: 1.1;
  }
  .person-role { font-size: 27px; font-weight: 600; color: var(--accent); letter-spacing: 1px; }
  .contact-list { position: absolute; left: 78px; top: 305px; list-style: none; }
  .contact-item {
    display: flex; align-items: center; gap: 16px; height: 42px;
    font-size: 26px; font-weight: 500; color: var(--text-light); letter-spacing: 1px;
  }
  .contact-icon { width: 30px; height: 30px; flex: none; }
  .social-row { position: absolute; left: 80px; top: 455px; display: flex; gap: 18px; }
  .social-dot { width: 46px; height: 46px; border-radius: 50%; background: var(--accent); }
  .back-emblem {
    position: absolute; left: 560px; top: 70px; width: 340px; height: 340px;
    border-radius: 50%;
    background: radial-gradient(circle at 50% 45%, var(--accent) 0%, #2a6f92 45%, var(--silver-dim) 100%);
    opacity: 0.85;
  }
</style>
</head>
<body>
<main class="sheet">
  <section class="card card--front" aria-label="Card front">
    <div class="front-emblem" role="img" aria-label="Company emblem"></div>
    <div class="front-wordmark">PLANKHORN</div>
  </section>

  <section class="card card--back" aria-label="Card back">
    <div class="back-wordmark">PLANKHORN</div>
    <div class="person">
      <p class="person-name">Darrel Sotho</p>
      <p class="person-role">Managing Partner</p>
    </div>
    <ul class="contact-list">
      <li class="contact-item">
        <svg class="contact-icon" viewBox="0 0 30 30" aria-hidden="true">
          <circle cx="15" cy="15" r="15" fill="#1fa3e0"/>
          <rect x="10" y="7" width="10" height="16" rx="2" fill="none" stroke="#121314" stroke-width="2"/>
          <circle cx="15" cy="20" r="1.2" fill="#121314"/>
        </svg>
        738-402-1954
      </li>
      <li class="contact-item">
        <svg class="contact-icon" viewBox="0 0 30 30" aria-hidden="true">
          <circle cx="15" cy="15" r="15" fill="#1fa3e0"/>
          <rect x="7" y="10" width="16" height="11" fill="none" stroke="#121314" stroke-width="2"/>
          <path d="M7 10 L15 17 L23 10" fill="none" stroke="#121314" stroke-width="2"/>
        </svg>
        Darrel@Plankhorn.com
      </li>
      <li class="contact-item">
        <svg class="contact-icon" viewBox="0 0 30 30" aria-hidden="true">
          <circle cx="15" cy="15" r="15" fill="#1fa3e0"/>
          <circle cx="15" cy="15" r="8" fill="none" stroke="#121314" stroke-width="1.8"/>
          <ellipse cx="15" cy="15" rx="3.5" ry="8" fill="none" stroke="#121314" stroke-width="1.5"/>
          <line x1="7" y1="15" x2="23" y2="15" stroke="#121314" stroke-width="1.5"/>
        </svg>
        Plankhorn.com
      </li>
    </ul>
    <div class="social-row" aria-label="Social links">
      <span class="social-dot"></span>
      <span class="social-dot"></span>
      <span class="social-dot"></span>
      <span class="social-dot"></span>
    </div>
    <div class="back-emblem" role="img" aria-label="Company emblem"></div>
  </section>
</main>
</body>
</html>
```